An our door sign really promoting our clinic and services

We have a new sports medicine clinic called HALLCREST SPORTS MEDICINE.
We want to make a really nice external sign at our clinic using a photo of our team we really like. I have attached the photo.
We want to simply include our LOGO and also signs with these slogan options. So we want different signs with these different slogans so we can choose what we really like.
This should be a simple and quite design.

The SLOGANS WE WOULD LIKE TO SEE ON THE SIGN (only one slogan per sign in the drafts)

1. Your Journey. Our Expertise
2. Where better health begins
3. Building the best version of you
4. Your health, in expert hands
5. Reaching new heights in your health
6. Your path to peak performance starts here

I have also included different versions of our logo based on the background and how you set the sign up

So summary
1. Image attached
2. Slogan options we would like to see them all
3. Logo attached (various options based on how you set the background up)
4. Size of sign is 2935mm wide x 1885mm high

```html
<!DOCTYPE html>
<html lang="en">
<head>
<meta charset="utf-8">
<title>Hallcrest Sports Medicine – Sign Drafts</title>
<link href="https://fonts.googleapis.com/css2?family=Poppins:wght@600;700&display=swap" rel="stylesheet">
<style>
  :root {
    --canvas: #bfc0c2;
    --navy-deep: #082050;
    --navy: #0c2f6e;
    --ring: #5aa9e6;
    --orange: #ff7a00;
    --amber: #ffb000;
    --white: #ffffff;
  }
  * { margin: 0; padding: 0; box-sizing: border-box; }
  html, body { width: 1200px; height: 583px; overflow: hidden; background: var(--canvas); }
  body { position: relative; font-family: "Poppins", sans-serif; }

  .art-defs { position: absolute; width: 0; height: 0; }

  .sign { position: absolute; width: 311px; height: 199px; overflow: hidden; }
  .sign-art { position: absolute; inset: 0; width: 100%; height: 100%; z-index: 0; }

  .brand { position: absolute; z-index: 2; left: 11px; top: 13px; display: flex; align-items: center; gap: 5px; color: var(--white); font-weight: 600; }
  .brand-dot { width: 14px; height: 14px; border-radius: 50%; background: var(--ring); }
  .brand-name { font-size: 11.5px; line-height: 1; letter-spacing: 0.3px; }
  .brand-sub { font-size: 5px; letter-spacing: 2px; line-height: 1.4; }

  .slogan { position: absolute; z-index: 2; font-weight: 700; text-transform: uppercase; white-space: nowrap;
    background: linear-gradient(180deg, var(--orange), var(--amber)); -webkit-background-clip: text; background-clip: text; color: transparent; }

  .s1 { left: 129px; top: 59px; }  .s2 { left: 452px; top: 59px; }  .s3 { left: 798px; top: 59px; }
  .s4 { left: 129px; top: 299px; } .s5 { left: 452px; top: 299px; } .s6 { left: 798px; top: 299px; }

  .s1 .slogan { left: 13px; top: 52px; font-size: 24px; line-height: 32px; }
  .s2 .slogan { right: 208px; top: 47px; text-align: right; font-size: 24px; line-height: 32px; }
  .s3 .slogan { left: 13px; top: 48px; font-size: 22px; line-height: 31px; }
  .s4 .slogan { left: 21px; top: 49px; font-size: 21.5px; line-height: 30px; }
  .s5 .slogan { left: 12px; top: 53px; font-size: 19px; line-height: 27px; }
  .s6 .slogan { left: 10px; top: 63px; font-size: 16px; line-height: 23px; }
</style>
</head>
<body>

<svg class="art-defs" aria-hidden="true">
  <defs>
    <linearGradient id="bg" x1="0" y1="0" x2="1" y2="1"><stop offset="0" stop-color="#0a2a64"/><stop offset="1" stop-color="#082050"/></linearGradient>
    <linearGradient id="ph" x1="0" y1="0" x2="1" y2="1"><stop offset="0" stop-color="#8e949c"/><stop offset="1" stop-color="#3a4352"/></linearGradient>
    <symbol id="sign-backdrop" viewBox="0 0 311 199">
      <rect width="311" height="199" fill="url(#bg)"/>
      <polygon points="120,199 311,40 311,199" fill="#0e3378"/>
      <polygon points="250,199 311,150 311,199" fill="#082050"/>
      <circle cx="228" cy="78" r="84" fill="none" stroke="#5aa9e6" stroke-width="0.8"/>
      <circle cx="228" cy="78" r="89" fill="none" stroke="#5aa9e6" stroke-width="0.8"/>
      <circle cx="228" cy="78" r="94" fill="none" stroke="#5aa9e6" stroke-width="0.8"/>
      <g role="img" aria-label="Photo of a clinician reviewing progress with an athlete in the gym">
        <circle cx="228" cy="78" r="77" fill="url(#ph)"/>
        <rect x="228" y="0" width="83" height="100" fill="url(#ph)"/>
      </g>
      <circle cx="311" cy="95" r="26" fill="#0c2a66"/>
      <circle cx="311" cy="95" r="18" fill="none" stroke="#5aa9e6" stroke-width="0.8"/>
      <circle cx="311" cy="95" r="12" fill="none" stroke="#5aa9e6" stroke-width="0.8"/>
      <circle cx="68" cy="199" r="25" fill="#0d3172"/>
      <circle cx="68" cy="199" r="19" fill="none" stroke="#4d8fd0" stroke-width="0.8"/>
      <circle cx="68" cy="199" r="13" fill="none" stroke="#4d8fd0" stroke-width="0.8"/>
    </symbol>
  </defs>
</svg>

<section class="sign s1">
  <svg class="sign-art" viewBox="0 0 311 199"><use href="#sign-backdrop"/></svg>
  <div class="brand"><span class="brand-dot"></span><div><div class="brand-name">HALLCREST</div><div class="brand-sub">SPORTS MEDICINE</div></div></div>
  <h2 class="slogan">Your<br>Journey<br>Our<br>Expertise</h2>
</section>

<section class="sign s2">
  <svg class="sign-art" viewBox="0 0 311 199"><use href="#sign-backdrop"/></svg>
  <div class="brand"><span class="brand-dot"></span><div><div class="brand-name">HALLCREST</div><div class="brand-sub">SPORTS MEDICINE</div></div></div>
  <h2 class="slogan">Where<br>Better<br>Health<br>Begins</h2>
</section>

<section class="sign s3">
  <svg class="sign-art" viewBox="0 0 311 199"><use href="#sign-backdrop"/></svg>
  <div class="brand"><span class="brand-dot"></span><div><div class="brand-name">HALLCREST</div><div class="brand-sub">SPORTS MEDICINE</div></div></div>
  <h2 class="slogan">Building<br>The Best<br>Version<br>Of You</h2>
</section>

<section class="sign s4">
  <svg class="sign-art" viewBox="0 0 311 199"><use href="#sign-backdrop"/></svg>
  <div class="brand"><span class="brand-dot"></span><div><div class="brand-name">HALLCREST</div><div class="brand-sub">SPORTS MEDICINE</div></div></div>
  <h2 class="slogan">Your<br>Health<br>In Expert<br>Hands</h2>
</section>

<section class="sign s5">
  <svg class="sign-art" viewBox="0 0 311 199"><use href="#sign-backdrop"/></svg>
  <div class="brand"><span class="brand-dot"></span><div><div class="brand-name">HALLCREST</div><div class="brand-sub">SPORTS MEDICINE</div></div></div>
  <h2 class="slogan">Reaching<br>New<br>Heights In<br>Your Health</h2>
</section>

<section class="sign s6">
  <svg class="sign-art" viewBox="0 0 311 199"><use href="#sign-backdrop"/></svg>
  <div class="brand"><span class="brand-dot"></span><div><div class="brand-name">HALLCREST</div><div class="brand-sub">SPORTS MEDICINE</div></div></div>
  <h2 class="slogan">Your Path<br>To Peak<br>Performance<br>Starts Here</h2>
</section>

</body>
</html>
```